Bref créative
KorvaLyne Stationary
Dennis Traven's cards
Professional
Dennis Traven, PhD, JD, MBA, MPM
Owner/Senior Consultant
PO Box 862
587E Harwick Rd
Thiensville, WI 53418-4471
dtraven@korvalyne-consulting.example
www.korvalyne-consulting.example
Working for answers to your academic problems. Together.
KorvaLyne-Consulting, LLC is proud to be a member of:
Gerald K Venn, Venn's consortium
Continental Guild of Learning Advisors and Presenters

```html
<!DOCTYPE html>
<html lang="en">
<head>
<meta charset="utf-8">
<title>KorvaLyne Consulting – Business Cards</title>
<link rel="stylesheet" href="https://fonts.googleapis.com/css2?family=Montserrat:wght@400;500;600;700&display=swap">
<style>
  :root {
    --bg: #e9e6e1;
    --card-teal: #1f5c60;
    --card-teal-dark: #143f43;
    --card-teal-light: #2a6d70;
    --ink-light: #ffffff;
    --ink-soft: #cfe3e2;
    --shadow: rgba(20, 30, 30, 0.25);
  }
  * { box-sizing: border-box; margin: 0; padding: 0; }
  html, body {
    width: 1200px;
    height: 629px;
    overflow: hidden;
    background: var(--bg);
    font-family: "Montserrat", sans-serif;
  }
  .sheet {
    position: relative;
    width: 1200px;
    height: 629px;
    display: flex;
    align-items: center;
    justify-content: center;
    gap: 50px;
  }
  .card {
    position: relative;
    width: 525px;
    height: 300px;
    border-radius: 4px;
    background: radial-gradient(ellipse at 50% 40%, var(--card-teal-light) 0%, var(--card-teal) 50%, var(--card-teal-dark) 100%);
    box-shadow: 0 10px 28px var(--shadow);
    color: var(--ink-light);
    overflow: hidden;
  }

  /* Brand lockup */
  .brand {
    display: flex;
    flex-direction: column;
    align-items: center;
    text-align: center;
  }
  .brand__dot {
    width: 64px;
    height: 64px;
    border-radius: 50%;
    background: var(--ink-light);
    margin-bottom: 10px;
  }
  .brand__name {
    font-weight: 600;
    font-size: 30px;
    line-height: 1.05;
    letter-spacing: -0.3px;
    color: var(--ink-light);
  }
  .brand__tagline {
    margin-top: 6px;
    font-size: 7px;
    font-weight: 400;
    letter-spacing: 0.3px;
    color: var(--ink-soft);
    max-width: 190px;
  }

  /* Front */
  .card--front {
    display: flex;
    align-items: center;
    justify-content: center;
  }

  /* Back */
  .card--back .brand {
    position: absolute;
    left: 36px;
    top: 58px;
    width: 190px;
  }
  .card--back .brand__dot { width: 74px; height: 74px; }
  .card--back .brand__name { font-size: 27px; }

  .contact {
    position: absolute;
    left: 268px;
    top: 42px;
    right: 24px;
  }
  .contact__name {
    font-size: 12.5px;
    font-weight: 600;
    line-height: 1.35;
  }
  .contact__role {
    font-size: 9px;
    font-weight: 400;
    color: var(--ink-soft);
    margin-top: 3px;
  }
  .contact__list {
    list-style: none;
    margin-top: 72px;
    font-size: 8.5px;
    line-height: 1.55;
  }
  .contact__item {
    display: flex;
    align-items: flex-start;
    gap: 7px;
    margin-bottom: 4px;
  }
  .contact__icon {
    flex: none;
    width: 10px;
    height: 10px;
    margin-top: 2px;
  }
  .membership {
    position: absolute;
    left: 24px;
    right: 24px;
    bottom: 14px;
    font-size: 6px;
    color: var(--ink-soft);
    text-align: center;
    letter-spacing: 0.2px;
  }
</style>
</head>
<body>
  <main class="sheet">
    <section class="card card--front" aria-label="Card front">
      <div class="brand">
        <span class="brand__dot"></span>
        <span class="brand__name">KorvaLyne<br>Consulting</span>
        <span class="brand__tagline">Working for answers to your academic problems. Together.</span>
      </div>
    </section>

    <section class="card card--back" aria-label="Card back">
      <div class="brand">
        <span class="brand__dot"></span>
        <span class="brand__name">KorvaLyne<br>Consulting</span>
        <span class="brand__tagline">Working for answers to your academic problems. Together.</span>
      </div>

      <div class="contact">
        <p class="contact__name">Dennis Traven, PhD,<br>JD, MBA, MPM</p>
        <p class="contact__role">Owner/Senior Consultant</p>
        <ul class="contact__list">
          <li class="contact__item">
            <svg class="contact__icon" viewBox="0 0 10 10" aria-hidden="true"><path d="M5 0.5a3.2 3.2 0 0 0-3.2 3.2C1.8 6 5 9.5 5 9.5S8.2 6 8.2 3.7A3.2 3.2 0 0 0 5 0.5z" fill="#fff"/><circle cx="5" cy="3.7" r="1.2" fill="#1f5c60"/></svg>
            <span>PO Box 862<br>587E Harwick Rd<br>Thiensville, WI 53418-4471</span>
          </li>
          <li class="contact__item">
            <svg class="contact__icon" viewBox="0 0 10 10" aria-hidden="true"><rect x="0.5" y="2" width="9" height="6.5" rx="0.8" fill="#fff"/><path d="M0.8 2.4 5 5.8l4.2-3.4" fill="none" stroke="#1f5c60" stroke-width="0.9"/></svg>
            <span>dtraven@korvalyne-consulting.example</span>
          </li>
          <li class="contact__item">
            <svg class="contact__icon" viewBox="0 0 10 10" aria-hidden="true"><circle cx="5" cy="5" r="4.3" fill="none" stroke="#fff" stroke-width="0.9"/><ellipse cx="5" cy="5" rx="1.9" ry="4.3" fill="none" stroke="#fff" stroke-width="0.8"/><path d="M0.7 5h8.6" stroke="#fff" stroke-width="0.8"/></svg>
            <span>www.korvalyne-consulting.example</span>
          </li>
        </ul>
      </div>

      <p class="membership">KorvaLyne-Consulting, LLC is proud to be a member of: Gerald K Venn, Venn's consortium · Continental Guild of Learning Advisors and Presenters</p>
    </section>
  </main>
</body>
</html>
```